Saucy Velvet Impz Business Card

We need business cards designed for our consultants to use and hand out to customers.
We are an Adult party plan company (like Crelvaware but sex toys and lingerie)
We would like bright colours pinks, purples.
The cards need our logo
Space for the reps phone number email address and name.
We need our website on it www.saucyvelvetimps.com.au

```html
<!DOCTYPE html>
<html lang="en">
<head>
<meta charset="utf-8">
<title>Saucy Velvet Impz Business Card</title>
<link rel="stylesheet" href="https://fonts.googleapis.com/css2?family=Great+Vibes&family=Lato:wght@400;700&family=Tinos&display=swap">
<style>
  :root {
    --pink: #e6399b;
    --white: #ffffff;
    --label: #222222;
    --edge: #e4e4e4;
  }
  * { margin: 0; padding: 0; box-sizing: border-box; }
  html, body { width: 1200px; height: 450px; overflow: hidden; background: var(--white); }
  .canvas { position: relative; width: 1200px; height: 450px; font-family: "Lato", sans-serif; }
  .side-label { position: absolute; top: 22px; font-family: "Tinos", serif; font-size: 22px; color: var(--label); }
  .side-label--front { left: 300px; }
  .side-label--back { left: 814px; }
  .card { position: absolute; left: 38px; top: 75px; width: 1124px; height: 345px; border: 1px solid var(--edge); overflow: hidden; }
  .card__front { position: absolute; left: 0; top: 0; width: 562px; height: 100%; background: var(--pink); }
  .card__back { position: absolute; left: 562px; top: 0; width: 562px; height: 100%; background: var(--white); }
  .figure-art { position: absolute; left: 516px; top: 0; width: 190px; height: 345px; }
  .brand { position: absolute; left: 0; width: 437px; top: 244px; text-align: right; color: var(--white); }
  .brand__name { font-weight: 700; font-size: 28px; line-height: 1; }
  .brand__tagline { margin-top: 8px; font-size: 12px; letter-spacing: 0.6px; text-transform: uppercase; }
  .contact { position: absolute; left: 562px; width: 562px; top: 78px; text-align: center; color: var(--pink); }
  .contact__name { font-family: "Great Vibes", cursive; font-size: 40px; line-height: 1.1; margin-bottom: 8px; }
  .contact__line { font-size: 19px; line-height: 27px; }
  .contact__web { font-weight: 700; font-size: 18px; }
</style>
</head>
<body>
<div class="canvas">
  <div class="side-label side-label--front">Front</div>
  <div class="side-label side-label--back">Back</div>

  <div class="card">
    <div class="card__front">
      <div class="brand">
        <div class="brand__name">Saucy Velvet Impz</div>
        <div class="brand__tagline">Your Playful Night In</div>
      </div>
    </div>
    <div class="card__back"></div>

    <svg class="figure-art" viewBox="0 0 190 345" role="img" aria-label="Silhouette of a kneeling figure spanning the fold of the card">
      <defs>
        <linearGradient id="figureTone" x1="0" y1="0" x2="1" y2="0">
          <stop offset="0" stop-color="#ffffff"/>
          <stop offset="0.5" stop-color="#f6b8dc"/>
          <stop offset="1" stop-color="#e6399b"/>
        </linearGradient>
      </defs>
      <rect x="0" y="0" width="190" height="345" rx="30" fill="url(#figureTone)"/>
    </svg>

    <div class="contact">
      <div class="contact__name">Name</div>
      <div class="contact__line">Saucy Velvet Impz Pty Ltd</div>
      <div class="contact__line">P.O. Box 418 Larkvale Vic 3199</div>
      <div class="contact__line">T: 0400 555 019</div>
      <div class="contact__line contact__web">www.saucyvelvetimps.com.au</div>
    </div>
  </div>
</div>
</body>
</html>
```